A label for my commercially sold local honey. This is a LABEL not a logo

3 inches high
2 inches wide

Target Market(s)

Customers who like "local" honey

Logo Text

Wildflower Honey -- 100% Pure & Unfiltered -- Florida

Logo styles of interest
Wordmark Logo
Requirements
Must have
• Wildflower Honey -- 100% Pure & Unfiltered -- Florida

Florida should be dominant

3 inches high / 2 inches wide

```html
<!DOCTYPE html>
<html lang="en">
<head>
<meta charset="utf-8">
<title>Wildflower Honey Label</title>
<link href="https://fonts.googleapis.com/css2?family=Uncial+Antiqua&family=Archivo+Black&display=swap" rel="stylesheet">
<style>
  :root {
    --backdrop: #ececec;
    --label-black: #0c0d0d;
    --flora-tone: #16181a;
    --honey-gold: #f0b418;
    --band-yellow: #fcbd14;
    --ink: #111111;
  }
  html, body {
    margin: 0;
    width: 1200px;
    height: 1200px;
    overflow: hidden;
    background: var(--backdrop);
  }
  .stage {
    position: relative;
    width: 1200px;
    height: 1200px;
  }
  .label {
    position: absolute;
    left: 300px;
    top: 150px;
    width: 600px;
    height: 900px;
    background: var(--label-black);
    overflow: hidden;
  }
  .flora-backdrop {
    position: absolute;
    inset: 0 0 130px 0;
    background: radial-gradient(ellipse at 50% 45%, var(--flora-tone) 0%, var(--label-black) 75%);
  }
  .brand-name {
    position: absolute;
    left: 0;
    right: 0;
    top: 150px;
    text-align: center;
    font-family: "Uncial Antiqua", serif;
    color: var(--honey-gold);
    font-size: 84px;
    line-height: 1.15;
    margin: 0;
  }
  .divider {
    position: absolute;
    left: 138px;
    top: 466px;
    width: 324px;
    height: 30px;
  }
  .product-name {
    position: absolute;
    left: 0;
    right: 0;
    top: 510px;
    margin: 0;
    text-align: center;
    font-family: "Uncial Antiqua", serif;
    font-weight: 400;
    color: var(--honey-gold);
    font-size: 62px;
    line-height: 82px;
    letter-spacing: 2px;
  }
  .product-name span { display: block; }
  .claim-pill {
    position: absolute;
    left: 52px;
    top: 700px;
    width: 496px;
    height: 24px;
    border-radius: 12px;
    background: var(--honey-gold);
    color: var(--ink);
    font-family: "Archivo Black", sans-serif;
    font-size: 14px;
    line-height: 24px;
    letter-spacing: 9px;
    text-align: center;
    text-indent: 9px;
  }
  .origin-band {
    position: absolute;
    left: 0;
    right: 0;
    bottom: 0;
    height: 130px;
    background: var(--band-yellow);
    display: flex;
    align-items: center;
    justify-content: center;
  }
  .origin-name {
    margin: 0;
    font-family: "Archivo Black", sans-serif;
    font-size: 62px;
    letter-spacing: 14px;
    text-indent: 14px;
    color: var(--ink);
  }
</style>
</head>
<body>
  <div class="stage">
    <section class="label">
      <div class="flora-backdrop" role="img" aria-label="Faint line drawing of wildflowers and bees"></div>
      <p class="brand-name">Palmetto<br>Hive</p>
      <svg class="divider" viewBox="0 0 324 30" aria-hidden="true">
        <path d="M2 24 Q162 4 322 24" fill="none" stroke="var(--honey-gold)" stroke-width="6" stroke-linecap="round"/>
      </svg>
      <h1 class="product-name"><span>Wildflower</span><span>Honey</span></h1>
      <div class="claim-pill">100% PURE &amp; UNFILTERED</div>
      <div class="origin-band">
        <h2 class="origin-name">FLORIDA</h2>
      </div>
    </section>
  </div>
</body>
</html>
```